BrightHarbor Flowchart Marketing Flyer

We are an MSP IT company. We have created a flowchart that we would like jazzed up to use in marketing new customers. The flowchart is a visual for prospective clients to see, in a simple way, what our process is. The flowchart should be 8.5"x11". We do not want the template of the flowchart altered (no boxes moved around) but would like something visually appealing and clean looking. Our office colors are lime green, royal blue, with accent colors of orange and purple. We would like the colors incorporated into the design. The design should be modern. This flyer is not going to be mass mailed. It will be handed to a prospective client in a face to face meeting.
Updates

I have uploaded our company logo to my brief in a couple of formats. One of the designers requested this. Great idea! I apologize for not providing it to begin with - it's my first time using this Website and the first time I have been assigned a project.

I was not able to view over the weekend as I did not have access to my work computer. Also need to review with the rest of management team on Thursday 6/28

Target Market(s)

Potential clients for an MSP IT company

Industry/Entity Type

It Company

Requirements
Must have
• The template itself we don't want changed. In other words we don't want the boxes moved around.
Nice to have
• Text, lines, shading and color of boxes can be changed. Not all colors mentioned in the brief need to be used. Would like it easy on the eye.

```html
<!DOCTYPE html>
<html lang="en">
<head>
<meta charset="utf-8">
<title>BrightHarbor Process Flyer</title>
<link href="https://fonts.googleapis.com/css2?family=Quicksand:wght@500;600;700&display=swap" rel="stylesheet">
<style>
  :root {
    --royal-blue: #1b4f9e;
    --lime: #5cc13a;
    --lime-soft: #cfeec3;
    --paper: #f3f4f5;
    --paper-edge: #e6e8ea;
    --white: #ffffff;
  }
  * { box-sizing: border-box; margin: 0; padding: 0; }
  html, body { width: 1200px; height: 1009px; overflow: hidden; }
  body {
    font-family: "Quicksand", sans-serif;
    background: radial-gradient(ellipse at 50% 40%, var(--paper) 0%, var(--paper-edge) 100%);
    position: relative;
    color: var(--royal-blue);
  }
  .shapes { position: absolute; inset: 0; }
  .title {
    position: absolute; top: 70px;
    font-weight: 700; color: var(--royal-blue); white-space: nowrap;
  }
  .title--process { left: 133px; font-size: 40px; top: 64px; }
  .title--ongoing { left: 615px; font-size: 29px; top: 78px; font-weight: 600; }
  .step { position: absolute; left: 200px; }
  .step__heading { font-size: 22px; font-weight: 600; color: var(--lime); }
  .step__list { list-style: none; margin-top: 6px; }
  .step__list li {
    font-size: 16px; font-weight: 600; color: var(--royal-blue);
    line-height: 29px; padding-left: 30px; position: relative;
  }
  .step__list li::before {
    content: ""; position: absolute; left: 5px; top: 10px;
    width: 9px; height: 9px; background: var(--royal-blue);
  }
  .step--assess { top: 174px; }
  .step--onboarding { top: 372px; }
  .step--evaluation { top: 580px; }
  .stage-label {
    position: absolute; left: 740px;
    font-size: 23px; font-weight: 600; color: var(--lime);
  }
  .outcomes {
    position: absolute; left: 630px; top: 772px; list-style: none;
  }
  .outcomes li {
    font-size: 22px; font-weight: 600; color: var(--royal-blue);
    line-height: 38px; padding-left: 26px; position: relative; white-space: nowrap;
  }
  .outcomes li::before {
    content: ""; position: absolute; left: 0; top: 14px;
    width: 9px; height: 9px; background: var(--royal-blue);
  }
  .brand {
    position: absolute; left: 128px; top: 845px;
    display: flex; align-items: center; gap: 16px;
  }
  .brand__dot {
    width: 40px; height: 40px; border-radius: 50%; background: var(--royal-blue);
  }
  .brand__name {
    font-size: 58px; font-weight: 700; color: var(--royal-blue); line-height: 1;
  }
</style>
</head>
<body>
<svg class="shapes" viewBox="0 0 1200 1009" width="1200" height="1009" aria-hidden="false">
  <defs>
    <style>
      .box { fill: var(--white); stroke: var(--lime); stroke-width: 2; }
      .box-shade { fill: var(--lime-soft); }
      .ring { fill: var(--white); stroke: var(--lime); stroke-width: 2; }
      .icon { fill: var(--lime); }
      .icon-line { stroke: var(--lime); stroke-width: 4; fill: none; stroke-linecap: round; stroke-linejoin: round; }
      .icon-blue { stroke: var(--royal-blue); stroke-width: 3; fill: none; stroke-linecap: round; stroke-linejoin: round; }
    </style>
  </defs>

  <!-- process steps -->
  <g class="process-steps">
    <path class="box-shade" d="M552 152 L592 247 L552 342 L560 342 L600 247 L560 152 Z"/>
    <path class="box" d="M130 147 L540 147 L580 242 L540 337 L130 337 Z"/>
    <path class="box-shade" d="M552 360 L592 454 L552 548 L560 548 L600 454 L560 360 Z"/>
    <path class="box" d="M130 355 L540 355 L580 449 L540 543 L130 543 Z"/>
    <path class="box-shade" d="M556 562 L596 657 L556 752 L564 752 L604 657 L564 562 Z"/>
    <path class="box" d="M133 557 L544 557 L584 652 L544 747 L133 747 Z"/>

    <circle class="ring" cx="126" cy="242" r="44"/>
    <g>
      <rect x="101" y="222" width="30" height="22" rx="2" class="icon-blue"/>
      <rect x="119" y="234" width="30" height="22" rx="2" fill="var(--white)" stroke="var(--lime)" stroke-width="3"/>
      <line x1="126" y1="242" x2="142" y2="242" class="icon-line" stroke-width="2"/>
      <line x1="126" y1="248" x2="142" y2="248" class="icon-line" stroke-width="2"/>
    </g>

    <circle class="ring" cx="126" cy="449" r="44"/>
    <rect x="106" y="429" width="40" height="40" rx="8" class="icon" role="img" aria-label="Icon of two people meeting at a table"/>

    <circle class="ring" cx="130" cy="652" r="44"/>
    <g>
      <rect x="119" y="622" width="16" height="14" class="icon"/>
      <rect x="119" y="645" width="16" height="14" class="icon"/>
      <rect x="119" y="668" width="16" height="14" class="icon"/>
      <path d="M122 628 l5 5 l12 -12" class="icon-blue"/>
      <path d="M122 651 l5 5 l12 -12" class="icon-blue"/>
      <path d="M122 674 l5 5 l12 -12" class="icon-blue"/>
    </g>
  </g>

  <!-- ongoing stages -->
  <g class="ongoing-stages">
    <path class="box-shade" d="M1026 146 L1050 206 L1026 266 L1032 266 L1056 206 L1032 146 Z"/>
    <path class="box" d="M655 140 L1014 140 L1040 206 L1014 270 L995 270 L985 281 L975 270 L655 270 Z"/>
    <path class="box-shade" d="M1026 299 L1050 357 L1026 419 L1032 419 L1056 357 L1032 299 Z"/>
    <path class="box" d="M655 293 L1014 293 L1040 357 L1014 423 L995 423 L985 434 L975 423 L655 423 Z"/>
    <path class="box-shade" d="M1026 455 L1050 513 L1026 575 L1032 575 L1056 513 L1032 455 Z"/>
    <path class="box" d="M655 449 L1014 449 L1040 513 L1014 579 L995 579 L985 590 L975 579 L655 579 Z"/>
    <path class="box-shade" d="M1026 605 L1050 665 L1026 725 L1032 725 L1056 665 L1032 605 Z"/>
    <path class="box" d="M655 599 L1014 599 L1040 665 L1014 729 L995 729 L985 740 L975 729 L655 729 Z"/>

    <circle class="ring" cx="657" cy="206" r="47"/>
    <rect x="637" y="186" width="40" height="40" rx="20" class="icon" role="img" aria-label="Icon of a strategist with an idea"/>

    <circle class="ring" cx="657" cy="357" r="47"/>
    <g>
      <path d="M643 335 L664 335 L672 343 L672 380 L643 380 Z" class="icon"/>
      <path d="M657 349 L666 366 L648 366 Z" fill="var(--white)"/>
      <line x1="657" y1="355" x2="657" y2="360" stroke="var(--lime)" stroke-width="2"/>
    </g>

    <circle class="ring" cx="657" cy="513" r="47"/>
    <rect x="637" y="493" width="40" height="40" rx="8" class="icon" role="img" aria-label="Icon of a hand holding a money bag"/>

    <circle class="ring" cx="657" cy="665" r="47"/>
    <g>
      <path d="M639 651 l6 4 l-6 4 Z M639 663 l6 4 l-6 4 Z M639 675 l6 4 l-6 4 Z" class="icon"/>
      <rect x="650" y="650" width="26" height="6" class="icon"/>
      <rect x="650" y="662" width="26" height="6" class="icon"/>
      <rect x="650" y="674" width="26" height="6" class="icon"/>
    </g>
  </g>
</svg>

<h1 class="title title--process">BrightHarbor Process</h1>
<h2 class="title title--ongoing">Ongoing Strategic Plan &amp; Execution</h2>

<section class="step step--assess">
  <h3 class="step__heading">Assess Alignment</h3>
  <ul class="step__list">
    <li>Review Technology Philosophy</li>
    <li>Share Proprietary Method</li>
    <li>Assess Organizational Fit</li>
  </ul>
</section>

<section class="step step--onboarding">
  <h3 class="step__heading">On Boarding</h3>
  <ul class="step__list">
    <li>Establish Expectations</li>
    <li>Service Provider Transition</li>
    <li>Cybersecurity Review</li>
    <li>Backup/Protection Strategy</li>
  </ul>
</section>

<section class="step step--evaluation">
  <h3 class="step__heading">30 Day Evaluation</h3>
  <ul class="step__list">
    <li>Develop IT Playbook</li>
    <li>Major Risk Identification</li>
    <li>Observe &amp; Document Trends</li>
    <li>Standards Alignment Plan</li>
  </ul>
</section>

<div class="stage-label" style="top:191px">Strategy</div>
<div class="stage-label" style="top:342px">Risk Assessment</div>
<div class="stage-label" style="top:498px">Budget</div>
<div class="stage-label" style="top:650px">Standards Alignment</div>

<ul class="outcomes">
  <li>Develop &amp; Execute Annual Strategic Plan</li>
  <li>Risk Assessment, Ranking, Mitigation</li>
  <li>Prioritize Investments</li>
  <li>Develop 5 Year Budget</li>
  <li>HarborSolutionTM Standard Alignment</li>
</ul>

<div class="brand">
  <span class="brand__dot"></span>
  <span class="brand__name">HarborIT</span>
</div>
</body>
</html>
```